Resident Guide for Senior Living Community

I need to create an informational magazine for residents that live in an Assisted Living community. This magazine is designed to educate the resident about the different service options and features that the community provides. I don't want to use any of the pictures in the Word Document - please use the uploaded picture instead. The final design should be both informational and elegant. The text in the word document is the actual text that needs to be used in the Resident Guide. Thanks!

Target Market(s)

Senior citizens and adult children (55 - 65 years old)

Industry/Entity Type

Assisted Living

Requirements
Must have
• Must be elegant - think Vellmore Orsay. Needs to have a lot of pictures and the logo must be used. The logo is the Plaque that says The Pellow Court.
Nice to have
• The Word doucment is the old Resident Guide - we are looking for a refresh using the same content.
Should not have
• please do not use any pictures from the Word Document other than the Logo.

```html
<!DOCTYPE html>
<html lang="en">
<head>
<meta charset="utf-8">
<title>The Pellow Court – Resident Guide</title>
<link href="https://fonts.googleapis.com/css2?family=Pinyon+Script&family=Source+Sans+3:ital,wght@0,400;0,600;0,700;0,800;1,400&display=swap" rel="stylesheet">
<style>
:root{
  --red:#a3303c;
  --red-soft:#c46a72;
  --green:#8db33a;
  --blue:#129bd5;
  --ink:#1f1f1f;
  --charcoal:#4a4a4a;
  --paper:#ffffff;
  --backdrop:#a7a7a7;
}
*{margin:0;padding:0;box-sizing:border-box}
html,body{width:1200px;height:1200px;overflow:hidden;background:var(--backdrop)}
body{font-family:"Source Sans 3",Arial,sans-serif;color:var(--ink)}
.stage{position:absolute;left:0;top:0;width:1500px;height:1500px;transform:scale(.8);transform-origin:0 0}
.page{position:absolute;background:var(--paper);width:490px;height:694px}
.abs{position:absolute}
.bar-red{background:var(--red)}
.tab{background:var(--red-soft)}
.rule-green{height:2px;background:var(--green)}
.running{font-size:9px;font-weight:800;letter-spacing:.3px;white-space:nowrap}
.running .script{font-family:"Pinyon Script",cursive;font-weight:400;font-size:13px;letter-spacing:0;margin-right:3px}
.photo{position:absolute}
.photo-edge{position:absolute;background:var(--green)}
.display{position:absolute;font-family:"Pinyon Script",cursive;font-size:32px;color:var(--charcoal);line-height:1;white-space:nowrap}
.heading{position:absolute;font-weight:800;font-size:18.5px;letter-spacing:.4px;line-height:22px;color:#222;white-space:nowrap}
.copy{position:absolute;font-size:7.7px;line-height:10px;text-align:justify;letter-spacing:-.1px}
.copy p{margin-bottom:7px}
.sub{color:var(--blue);font-weight:800;font-size:9px;line-height:11px;margin-top:2px}
.drop{float:left;font-size:34px;line-height:28px;color:var(--blue);font-style:italic;margin:2px 4px 0 0}
.note{font-style:italic}
.bold{font-weight:700}
.folio{position:absolute;font-size:9px;font-weight:800}
.footer-tab{position:absolute;height:28px;background:var(--blue);color:#fff;font-size:7.5px;font-weight:800;text-align:center;line-height:20px;border-radius:4px 4px 0 0}
.footer-tab span{font-weight:400}
.levels-panel{position:absolute;background:#4b4b4b;color:#fff;font-size:7px;font-style:italic;text-align:center;line-height:10px;padding:4px 20px 0 32px}
.levels-panel .edge{position:absolute;left:0;top:0;bottom:0;width:15px;background:var(--green)}
.levels-panel p{margin-bottom:4px}
ul.bullets{list-style:none}
ul.bullets li{position:relative;padding-left:10px;margin-bottom:7px}
ul.bullets li::before{content:"•";position:absolute;left:0}
ul.bullets li.sub-item{padding-left:19px}
ul.bullets li.sub-item::before{content:"-";left:10px}
.plaque{position:absolute;display:flex;align-items:center;gap:6px;font-weight:700;font-size:11px;color:#8a6d12}
.plaque .mark{width:22px;height:22px;background:#c9a227}
</style>
</head>
<body>
<div class="stage">

  <!-- ========== SPREAD 1 : page 10 ========== -->
  <section class="page" style="left:271px;top:42px">
    <div class="abs bar-red" style="left:0;top:21px;width:47px;height:5px"></div>
    <div class="abs running" style="left:54px;top:16px"><span class="script">Resident</span>INFORMATION</div>
    <div class="abs rule-green" style="left:169px;top:23px;width:67px"></div>

    <div class="photo" role="img" aria-label="Bright resident bedroom with white bedding, dresser and lamp" style="left:47px;top:48px;width:382px;height:206px;background:linear-gradient(135deg,#cbb69a,#efe6d8 45%,#d9c7ad)"></div>
    <div class="photo-edge" style="left:429px;top:48px;width:14px;height:206px"></div>

    <div class="abs tab" style="left:0;top:276px;width:38px;height:25px"></div>
    <div class="display" style="left:44px;top:272px">Penthouse Apartments,</div>
    <div class="heading" style="left:46px;top:310px">SANDY SPRINGS WITH HEALTH CARE<br>AND HOSPITALITY SERVICES</div>
    <div class="abs bar-red" style="left:362px;top:310px;width:81px;height:48px"></div>

    <div class="copy" style="left:46px;top:373px;width:190px">
      <p><span class="drop">T</span>he Pellow Court is proud to offer a limited number of exclusive Penthouses in Alder Springs unique in the world of high level care Assisted Living. We also offer two (2) room apartment units in Brookfield.</p>
      <div class="sub">THE ASHEVILLE PENTHOUSE</div>
      <p>One luxurious bedroom with handicap equipped bath and shower, full kitchen, living room, private balcony. ($8500 per month* single occupancy)</p>
      <div class="sub">THE CHARLESTON PENTHOUSE</div>
      <p>One large bedroom with bath, living room, full kitchen, and a large sun deck. ($9500 per month* single occupancy)</p>
      <div class="sub">THE EDEN PENTHOUSE</div>
      <p>One bedroom with bath, full kitchen, living room, private balcony. ($11,500 per month* single occupancy)</p>
      <div class="sub">THE DURHAM PENTHOUSES</div>
      <p>Two bedrooms, with two baths (one handicap equipped bath), full kitchen w/ pantry, living room, private balcony. Note: Unit may be rented as two separate units (see below) ($11,500 per month*)</p>
      <p class="bold">Durham A (single)--$8000<br>Durham B (single)--$6500</p>
    </div>

    <div class="copy" style="left:254px;top:373px;width:190px">
      <div class="sub">THE BERKSHIRE PENTHOUSES</div>
      <p>Larkmoor's finest. Two bedrooms, two baths, walk-in closet, living room with fireplace and bay window, full kitchen, dining room, large deck, screened porch. ($13,000 per month*) single occupancy.</p>
      <p class="bold">Berkshire A--$7000 - Single Occupancy<br>Berkshire B--$7000 - Single Occupancy</p>
      <p class="note">*All prices quoted for single occupancy. Second person adds $7,500 per month, including meals, as long as second occupant requires no health care or assisted living needs. (Available at additional charge.)</p>
    </div>

    <div class="photo" role="img" aria-label="Sunlit living room with sofa, armchairs and bay windows" style="left:254px;top:511px;width:175px;height:135px;background:linear-gradient(160deg,#e8ddc9,#c9b59a 55%,#8fa8a2)"></div>
    <div class="photo-edge" style="left:429px;top:511px;width:14px;height:135px"></div>

    <div class="folio" style="left:35px;top:665px">10</div>
    <div class="footer-tab" style="left:181px;top:666px;width:128px">THE PELLOW COURT <span>- SINCE 1988</span></div>
  </section>

  <!-- ========== SPREAD 1 : page 11 ========== -->
  <section class="page" style="left:761px;top:42px">
    <div class="abs rule-green" style="left:254px;top:23px;width:68px"></div>
    <div class="abs running" style="left:328px;top:16px"><span class="script">Resident</span>INFORMATION</div>
    <div class="abs bar-red" style="left:444px;top:21px;width:46px;height:5px"></div>

    <div class="abs tab" style="left:0;top:58px;width:43px;height:24px"></div>
    <div class="display" style="left:50px;top:52px">Service</div>
    <div class="heading" style="left:53px;top:88px">LEVELS &amp; FEES, BROOKFIELD</div>
    <div class="abs bar-red" style="left:350px;top:86px;width:93px;height:24px"></div>

    <div class="copy" style="left:46px;top:123px;width:190px">
      <p><span class="drop">T</span>he Pellow Court is an exclusive State of Georgia, Licensed Assisted Living healthcare residence (founded by the Pellow Family in 1988) for persons who require significantly higher levels of healthcare and ancillary hospitality services to remain as independent as possible. To apply for residence and to ascertain</p>
    </div>
    <div class="copy" style="left:254px;top:123px;width:190px">
      <p>with you the appropriate and necessary combination of ADL's (activities-of-daily- living) and personal and assisted living hands-on health care services and their costs, an assessment will be scheduled with our Director of Healthcare Services.</p>
    </div>

    <div class="abs tab" style="left:0;top:209px;width:43px;height:24px"></div>
    <div class="display" style="left:50px;top:203px">Health</div>
    <div class="heading" style="left:53px;top:241px">CARE PROGRAM LEVELS</div>
    <div class="abs bar-red" style="left:273px;top:238px;width:170px;height:24px"></div>

    <div class="copy" style="left:46px;top:280px;width:190px">
      <div class="sub">SILVER LEVEL 1 SERVICE - $4000.00/<br>MONTH $132 /DAY</div>
      <p>24 hour moderate assistance with activities-of-daily-living (ADL's) which customarily include eating assistance, dressing, toileting, grooming, bathing, walking, maintaining continence, medication supervision, hospitality and dining services (our "Silver Tray" Service included), reminders for meals and activities, ambulation with walker or wheelchair. Includes early stage Alzheimer's/dementia and memory care management and supervision.</p>
      <div class="sub">GOLD LEVEL 2 SERVICE - $5000.00/<br>MONTH $164 /DAY</div>
      <p>Progressive 24 hour assistance with ADL's covers a higher level of hands-on personal care and interdisciplinary care services, incontinence management, assistance</p>
    </div>
    <div class="copy" style="left:254px;top:280px;width:190px">
      <p>with transfers, diabetes monitoring/glucose checks and insulin, and assistance with eating (our "Silver Tray" Service included). Includes care for advancing Alzheimer's/dementia and memory issues.</p>
      <p class="bold">Platinum Levels 3 Service - $6000.00/month $197 /day<br>Platinum Levels 4 Service - $6500.00/month $214 /day</p>
      <p>Our two most advanced levels of 24 hour assistance with ADL's includes intensive 24/7 personal health care. Includes advanced Alzheimer's/dementia with incontinence management, assistance with transfers, behavioral issues such as agitation, wandering, elopement, insomnia, diabetes monitoring/glucose checks and insulin, and assistance with eating (our "Silver Tray" Service included). Includes late stage Alzheimer's/dementia and acute memory issues.</p>
    </div>

    <div class="levels-panel" style="left:46px;top:469px;width:397px;height:52px">
      <div class="edge"></div>
      <p>LEVEL 3 - IN EACH HOME'S SPECIAL ERP MD SPECIAL CARE ANNEX, AS DETERMINED<br>BY OUR ASSESSMENT AND DISCUSSION WITH THE FAMILY.</p>
      <p>LEVEL 4 - IN EACH HOME'S SPECIAL ERP MD SPECIAL CARE ANNEX, AS DETERMINED<br>BY OUR ASSESSMENT AND DISCUSSION WITH THE FAMILY.</p>
    </div>

    <div class="abs tab" style="left:0;top:549px;width:43px;height:25px"></div>
    <div class="display" style="left:50px;top:544px">Respite <span style="font-family:'Source Sans 3',sans-serif;font-weight:800;font-size:18.5px;color:#222">CARE</span></div>
    <div class="abs bar-red" style="left:194px;top:549px;width:249px;height:25px"></div>

    <div class="copy" style="left:46px;top:588px;width:190px">
      <p><span class="drop">F</span>rom time to time, on a space available basis, The Pellow Court will accept persons on a short-term respite basis. This may be strictly for the respite benefits of a resident and/or his/her family or preliminary to permanent residence in The Pellow Court. (Assessment required.)</p>
    </div>
    <div class="copy" style="left:254px;top:588px;width:190px">
      <p>The rate is $350 per-day all-inclusive, on an as available basis. Minimum stay is one week. Payable in advance. One month minimum if rental furniture required. Standard security deposit required.</p>
    </div>

    <div class="folio" style="left:444px;top:665px">11</div>
    <div class="footer-tab" style="left:182px;top:666px;width:128px">THE PELLOW COURT <span>- SINCE 1988</span></div>
  </section>

  <!-- ========== SPREAD 2 : page 12 ========== -->
  <section class="page" style="left:271px;top:770px">
    <div class="abs bar-red" style="left:0;top:21px;width:47px;height:5px"></div>
    <div class="abs running" style="left:54px;top:16px"><span class="script">Resident</span>INFORMATION</div>
    <div class="abs rule-green" style="left:169px;top:23px;width:67px"></div>

    <div class="photo" role="img" aria-label="Plated grilled chicken sandwich with berries beside wine glasses" style="left:47px;top:47px;width:382px;height:206px;background:linear-gradient(135deg,#3a1d14,#8b5a35 40%,#e9e1d4 70%,#7a3024)"></div>
    <div class="photo-edge" style="left:429px;top:47px;width:14px;height:206px"></div>

    <div class="abs tab" style="left:0;top:270px;width:38px;height:24px"></div>
    <div class="display" style="left:44px;top:264px">All Levels</div>
    <div class="heading" style="left:46px;top:305px">OF HEALTH CARE PROGRAMS INCLUDE</div>
    <div class="abs bar-red" style="left:380px;top:303px;width:63px;height:25px"></div>

    <div class="copy" style="left:46px;top:347px;width:190px;text-align:left">
      <p style="text-align:justify"><span class="drop">A</span>ssistance with all medications as often as ordered by your physician. Coordination of outside health care providers including:</p>
      <ul class="bullets">
        <li>Attending physician</li>
        <li>Home Health (private pay available from PellowCare)</li>
        <li>In Your Own Home Hospice Care (we own the two (2) Hospice in-patient units next door to each Pellow Court)</li>
        <li class="sub-item">Pharmacy</li>
        <li class="sub-item">Podiatrist</li>
        <li class="sub-item">Psychologist</li>
        <li class="sub-item">Psychiatrist</li>
        <li>Full daily activity schedule programmed to allow each resident's functional ability and attention level to be maximized.</li>
        <li>Laundry services three (3) times per week, or as needed.</li>
        <li>Emergency call system in each bedroom and bathroom.</li>
        <li>Our Signature "Silver Tray Room Service" when a resident is not able, or chooses not, to join us in the dining room.</li>
      </ul>
    </div>
    <div class="copy" style="left:254px;top:347px;width:190px;text-align:left">
      <ul class="bullets">
        <li>Housekeeping services a minimum of twice per week. More often as needed.</li>
        <li>All utilities included except telephone and cable. Units wired for service. No extra charge for wireless.</li>
        <li>Special diets available including:</li>
        <li class="sub-item">Diabetic</li>
        <li class="sub-item">Low salt</li>
        <li class="sub-item">Soft mechanical Gluten free</li>
        <li>Bottled water and soft drinks to enjoy upon request.</li>
        <li>Multiple common rooms for the resident/resident family's enjoyment:</li>
        <li class="sub-item">Large living rooms with cathedral ceiling and fireplaces</li>
        <li class="sub-item">Screened porches overlooking wooded areas (The Pellow Court- Alder Springs)</li>
        <li class="sub-item">Enclosed courtyards with tables, chairs and gazebos, game rooms, family rooms with fireplace, and beauty/barber salon</li>
        <li>Private dining areas available for special family celebrations.</li>
        <li>A variety of nutritious snacks and goodies provided between meals from The Pellow Court Kitchens.</li>
      </ul>
    </div>

    <div class="folio" style="left:35px;top:665px">12</div>
    <div class="footer-tab" style="left:181px;top:666px;width:128px">THE PELLOW COURT <span>- SINCE 1988</span></div>
  </section>

  <!-- ========== SPREAD 2 : page 13 ========== -->
  <section class="page" style="left:761px;top:770px">
    <div class="abs rule-green" style="left:254px;top:23px;width:68px"></div>
    <div class="abs running" style="left:328px;top:16px"><span class="script">Resident</span>INFORMATION</div>
    <div class="abs bar-red" style="left:444px;top:21px;width:46px;height:5px"></div>

    <div class="abs tab" style="left:0;top:182px;width:44px;height:24px"></div>
    <div class="display" style="left:55px;top:176px">Our <span style="font-family:'Source Sans 3',sans-serif;font-weight:800;font-size:18.5px;color:#222">HERITAGE</span></div>
    <div class="abs bar-red" style="left:199px;top:182px;width:245px;height:24px"></div>

    <div class="copy" style="left:46px;top:228px;width:190px">
      <p><span class="drop">E</span>ach phase of life, aging or health issues carries its own challenges. So we are here with strength and support, uniquely equipped to assist you with the great majority of your loved one's needs. And that's among the many reasons people choose The Pellow Court over other options in the region. We have a distinguished record of serving residents and families for thirty years. This makes us the most experienced provider of Alzheimer's and advanced Memory Care in a residential setting in our region.</p>
      <p>Our founder's father, Dr. Edwin R. Pellow Jr. was the inspiration for The Pellow Court. He was a Doctor of Public Health and a nationally prominent physician, educator and pharmaceutical research executive.</p>
    </div>
    <div class="copy" style="left:254px;top:228px;width:190px">
      <p>His exemplary inspiration, dedication and lifelong pursuit of medical answers for some of humanity's most destructive diseases, along with his personal struggle with Alzheimer's over 17 years, is the legacy of The Pellow Court.</p>
    </div>

    <div class="plaque" style="left:255px;top:325px;width:126px;height:30px">
      <span class="mark"></span>The Pellow Court
    </div>

    <div class="photo" role="img" aria-label="Stone entrance with double wooden doors, lanterns and potted hydrangeas" style="left:61px;top:396px;width:382px;height:251px;background:linear-gradient(135deg,#8c7d6a,#b8a890 40%,#5a3a22 60%,#a99a86)"></div>
    <div class="photo-edge" style="left:47px;top:396px;width:14px;height:251px"></div>

    <div class="folio" style="left:444px;top:665px">13</div>
    <div class="footer-tab" style="left:182px;top:666px;width:128px">THE PELLOW COURT <span>- SINCE 1988</span></div>
  </section>

</div>
</body>
</html>
```